First Aid Training business needs business card design

We would like a double sided business card designed for a first aid training business - Brindlewood First Aid. We provide first aid training and , WHS (work, health and safety) training.

The attached word document contains the key information we would like on each side of the business card.

Final design needs to be delivered in print ready format, along with the original file.

```html
<!DOCTYPE html>
<html lang="en">
<head>
<meta charset="utf-8">
<title>Brindlewood First Aid – Business Card</title>
<link rel="stylesheet" href="https://fonts.googleapis.com/css2?family=Montserrat:wght@500;600&display=swap">
<style>
  :root {
    --page-bg: #cccccc;
    --card-bg: #ffffff;
    --wave: #808080;
    --ink: #333333;
    --ink-dark: #111111;
    --accent: #ee1c1c;
  }
  * { margin: 0; padding: 0; box-sizing: border-box; }
  html, body { width: 1000px; height: 1200px; overflow: hidden; }
  body {
    background: var(--page-bg);
    font-family: "Montserrat", sans-serif;
    color: var(--ink);
    position: relative;
  }
  .card {
    position: absolute;
    left: 51px;
    width: 898px;
    height: 538px;
    background: var(--card-bg);
    overflow: hidden;
  }
  .card--front { top: 44px; }
  .card--back { top: 616px; }
  .card__waves { position: absolute; inset: 0; width: 100%; height: 100%; }
  .card__waves path { fill: var(--wave); }

  .brand-mark {
    position: absolute;
    border-radius: 50%;
    background: var(--accent);
  }
  .brand-name {
    position: absolute;
    font-weight: 600;
    color: var(--ink-dark);
    line-height: 1.15;
  }
  .card--front .brand-mark { left: 176px; top: 112px; width: 120px; height: 120px; }
  .card--front .brand-name { left: 40px; top: 290px; width: 380px; text-align: center; font-size: 36px; }

  .contact { position: absolute; left: 462px; top: 312px; }
  .contact__name { font-size: 31px; font-weight: 600; line-height: 1; margin-bottom: 17px; }
  .contact__row {
    display: flex; align-items: center; gap: 10px;
    font-size: 22px; font-weight: 600; line-height: 1; height: 39px;
  }
  .contact__icon {
    width: 22px; height: 22px; border-radius: 3px;
    background: var(--wave); flex: none;
  }
  .contact__icon svg { display: block; width: 22px; height: 22px; }

  .benefits { position: absolute; left: 68px; top: 124px; font-size: 27px; font-weight: 600; line-height: 41.5px; }
  .benefits li { list-style: none; }
  .benefits li::before { content: "•"; }

  .card--back .brand-mark { left: 72px; top: 350px; width: 108px; height: 108px; }
  .card--back .brand-name { left: 215px; top: 384px; font-size: 28px; white-space: nowrap; }
  .services { position: absolute; left: 583px; top: 367px; font-size: 27px; font-weight: 600; line-height: 40px; }
</style>
</head>
<body>

<section class="card card--front">
  <svg class="card__waves" viewBox="0 0 898 538" preserveAspectRatio="none" aria-hidden="true">
    <path d="M0 0 H898 V66 C820 90 760 88 640 70 C480 45 330 10 200 24 C120 33 60 46 0 64 Z"/>
    <path d="M0 471 C80 452 160 448 240 456 C400 472 560 525 740 518 C800 515 850 490 898 473 V538 H0 Z"/>
  </svg>

  <div class="brand-mark" aria-hidden="true"></div>
  <div class="brand-name">Brindlewood First Aid</div>

  <div class="contact">
    <p class="contact__name">Daniel Hargreave</p>
    <p class="contact__row">
      <span class="contact__icon"><svg viewBox="0 0 22 22"><path d="M7 5 L9.5 5 L10.5 8.5 L9 10 C9.8 11.8 10.6 12.7 12 13.5 L13.5 12 L17 13 L17 15.5 C17 16.3 16.3 17 15.5 17 C10 16.6 5.4 12 5 6.5 C5 5.7 5.7 5 6.5 5 Z" fill="#fff"/></svg></span>
      0491 570 226
    </p>
    <p class="contact__row">
      <span class="contact__icon"><svg viewBox="0 0 22 22"><rect x="4" y="6" width="14" height="10" fill="none" stroke="#fff" stroke-width="1.5"/><path d="M4 6 L11 12 L18 6 M4 16 L9 11 M18 16 L13 11" fill="none" stroke="#fff" stroke-width="1.3"/></svg></span>
      help@brindlewoodfa.com.au
    </p>
    <p class="contact__row">
      <span class="contact__icon"><svg viewBox="0 0 22 22"><g fill="none" stroke="#fff" stroke-width="1.3"><circle cx="11" cy="11" r="6.5"/><ellipse cx="11" cy="11" rx="3" ry="6.5"/><path d="M4.5 11 H17.5 M5.5 8 H16.5 M5.5 14 H16.5"/></g></svg></span>
      brindlewoodfa.com.au
    </p>
  </div>
</section>

<section class="card card--back">
  <svg class="card__waves" viewBox="0 0 898 538" preserveAspectRatio="none" aria-hidden="true">
    <path d="M0 0 H898 V64 C840 44 790 22 700 22 C560 24 420 60 280 80 C180 92 100 88 0 60 Z"/>
    <path d="M0 474 C80 500 160 516 250 516 C420 512 560 470 720 457 C800 452 850 462 898 474 V538 H0 Z"/>
  </svg>

  <ul class="benefits">
    <li style="list-style:none">Onsite Training – We can come to you</li>
    <li>Time efficient</li>
    <li>Cost effective</li>
    <li>Minimise downtime for your team</li>
  </ul>

  <div class="brand-mark" aria-hidden="true"></div>
  <div class="brand-name">Brindlewood First Aid</div>

  <div class="services">
    <p>First Aid Training</p>
    <p>WHS Training</p>
  </div>
</section>

</body>
</html>
```